Acrylic print memorial plaque for entrance

I need a design for an acrylic print in DIN A0 portrait format or 1.5x DIN A0.

The top 40% should contain the lettering "Veronika's Meadow Haven." The lettering should frame three pictures. In the center is a portrait of Vero (Veronika), with "In Memoriam" below the name and the dates *November 20, 1980 †May 15, 2024. The head of the horse Solvina should be placed on the left, and Bellis's head on the right.
The next 35% of the area should depict the portraits of Gerhard (left), Henrik (middle), and Frieda (right) in the upper part. Each with their name underneath. The lower part of this 35% should contain

“Our helpers:”
Then the portraits of Dieter, Helene, Uschi & Glenn should be taken in the following order. Each one should also have its name underneath the portrait.
The remaining 25% should contain the following:
“We would like to thank:
Klaus & Ingrid for their valuable support, and Hanni for her help and tips on handling the horse. We would also like to thank the Weibel family, especially Beni & Sabine and Flori & Greta, for allowing us to create this paradise according to our ideas and for the construction. And, of course, the many other helpers and supporters.
The images should be isolated as much as possible and scaled to fit the print size. If possible, only the faces (head + neck) should be included.

Cut out, shape, or mirror the horse heads depending on the design.

The various images can be used as backgrounds, provided the design allows it.

Target Market(s)

No target mark, memorial plaque for the stable

Font styles to use
Serif
Decorative
Script

Requirements
Must have
• Honest, Authentic, Devotional
Should not have
• Kitsch, too playful.

```html
<!DOCTYPE html>
<html lang="de">
<head>
<meta charset="utf-8">
<title>Veronika's Meadow Haven – In Memoriam</title>
<link rel="stylesheet" href="https://fonts.googleapis.com/css2?family=Cinzel:wght@400;600;700&family=EB+Garamond:wght@400;500&family=Lobster&display=swap">
<style>
  :root {
    --navy: #17206b;
    --navy-deep: #0f1650;
    --gold: #b08a4a;
    --gold-light: #d8b679;
    --sky-top: #d9f3fb;
    --sky-mid: #a9e0f3;
    --sky-soft: #c6ecf8;
    --sand: #ead8bb;
    --sand-light: #f3e6d0;
    --ink: #1d1d24;
    --photo-bg: #e9e6e2;
  }
  * { box-sizing: border-box; margin: 0; padding: 0; }
  html, body { width: 1090px; height: 1200px; overflow: hidden; background: #f4f4f4; }

  .plaque {
    position: relative;
    width: 1090px;
    height: 1200px;
    overflow: hidden;
    background:
      radial-gradient(ellipse 420px 300px at 180px 560px, rgba(120,200,235,.55), transparent 70%),
      radial-gradient(ellipse 380px 260px at 900px 420px, rgba(150,215,240,.5), transparent 70%),
      radial-gradient(ellipse 500px 300px at 540px 760px, rgba(140,210,238,.45), transparent 70%),
      linear-gradient(180deg, var(--sky-top) 0%, var(--sky-mid) 45%, var(--sky-soft) 80%, var(--sky-soft) 100%);
  }
  .sand-band {
    position: absolute; left: 0; right: 0; bottom: 0; height: 190px;
    background: linear-gradient(180deg, rgba(234,216,187,0) 0%, var(--sand-light) 16%, var(--sand) 60%, #e2cba6 100%);
  }
  .border-frame { position: absolute; inset: 0; pointer-events: none; }

  .title { position: absolute; left: 0; right: 0; text-align: center; font-family: 'Lobster', cursive; }
  .title-name {
    top: 30px; font-size: 88px; line-height: 1; color: var(--navy);
    text-shadow: 3px 3px 0 #fff, -1px -1px 0 #fff, 4px 5px 0 #e0c9a0;
  }
  .title-place {
    top: 120px; font-size: 54px; line-height: 1; color: var(--gold-light);
    text-shadow: 2px 2px 0 #fff, 3px 4px 0 #8a6a36;
  }

  .horse { position: absolute; top: 128px; width: 270px; height: 210px; }
  .horse-left {
    left: 30px;
    background: radial-gradient(ellipse at 70% 60%, #3b302b, #241c19 70%, rgba(36,28,25,.2));
    border-radius: 10px 70% 40% 10px;
  }
  .horse-right {
    right: 30px;
    background: radial-gradient(ellipse at 30% 60%, #b5582b, #8c3c1c 70%, rgba(140,60,28,.2));
    border-radius: 70% 10px 10px 40%;
  }
  .horse-label {
    position: absolute; top: 352px; font-family: 'Cinzel', serif; font-size: 15px; line-height: 20px;
    letter-spacing: 5px; color: var(--ink);
  }
  .horse-label-left { left: 62px; }
  .horse-label-right { right: 50px; }

  .portrait-ring {
    position: absolute; left: 395px; top: 203px; width: 290px; height: 290px;
    border: 1.5px solid var(--gold); border-radius: 50%;
  }
  .portrait {
    position: absolute; left: 408px; top: 210px; width: 272px; height: 272px; border-radius: 50%;
    background: radial-gradient(circle at 50% 45%, #d9b9a2 0%, #b58f79 40%, #4a3a33 100%);
  }
  .memorial-heading {
    position: absolute; top: 512px; left: 0; right: 0; text-align: center;
    font-family: 'Lobster', cursive; font-size: 70px; color: var(--navy-deep); line-height: 1;
  }
  .dates {
    position: absolute; top: 596px; left: 310px; width: 470px; height: 40px;
    border-top: 1.5px solid var(--gold); border-bottom: 1.5px solid var(--gold);
    text-align: center; font-family: 'EB Garamond', serif; font-size: 21px; line-height: 37px; color: var(--ink);
  }
  .dates sup { font-size: 12px; }

  .section-title {
    position: absolute; left: 0; right: 0; display: flex; align-items: center; justify-content: center; gap: 14px;
    font-family: 'Cinzel', serif; font-weight: 600; font-size: 24px; line-height: 30px; letter-spacing: 7px; color: var(--gold);
  }
  .section-title::before, .section-title::after {
    content: ""; width: 70px; height: 1.5px; background: var(--gold);
  }
  .section-families { top: 654px; }
  .section-helpers { top: 845px; }

  .person { position: absolute; width: 160px; text-align: center; }
  .person-photo {
    margin: 0 auto; border-radius: 50%; border: 1.5px solid var(--gold);
    background: radial-gradient(circle at 50% 42%, #d7b4a0 0%, #b48c78 45%, #8c7a6a 100%);
  }
  .family { top: 692px; }
  .family .person-photo { width: 100px; height: 100px; }
  .helper { top: 882px; }
  .helper .person-photo { width: 88px; height: 88px;
    background: radial-gradient(circle at 50% 42%, #d9b6a0 0%, #b58c76 40%, #5f7d4f 100%); }
  .person-name {
    margin-top: 8px; font-family: 'Cinzel', serif; font-size: 19px; line-height: 24px; letter-spacing: 1.5px; color: var(--ink);
  }
  .helper .person-name { font-size: 18px; }

  .thanks-heading {
    position: absolute; top: 1024px; left: 0; right: 0; text-align: center;
    font-family: 'Cinzel', serif; font-weight: 700; font-size: 30px; line-height: 38px; color: var(--navy);
  }
  .thanks-text {
    position: absolute; top: 1066px; left: 80px; right: 80px; text-align: center;
    font-family: 'EB Garamond', serif; font-size: 18px; line-height: 22px; color: var(--ink);
  }
</style>
</head>
<body>
<main class="plaque">
  <div class="sand-band" role="img" aria-label="Sandstrand im unteren Bereich"></div>

  <svg class="border-frame" width="1090" height="1200" viewBox="0 0 1090 1200" aria-hidden="true">
    <g fill="none" stroke="#b08a4a">
      <rect x="14" y="14" width="1062" height="1172" stroke-width="2"/>
      <rect x="22" y="22" width="1046" height="1156" stroke-width="1"/>
      <path d="M34 70 V34 H120" stroke-width="1.5"/>
      <path d="M1056 70 V34 H970" stroke-width="1.5"/>
      <path d="M34 1130 V1166 H120" stroke-width="1.5"/>
      <path d="M1056 1130 V1166 H970" stroke-width="1.5"/>
    </g>
  </svg>

  <h1 class="title title-name">Veronika’s</h1>
  <p class="title title-place">Meadow Haven</p>

  <div class="horse horse-left" role="img" aria-label="Kopf des Pferdes Solvina, dunkelbraun, nach rechts blickend"></div>
  <div class="horse horse-right" role="img" aria-label="Kopf des Pferdes Bellis, fuchsfarben, nach links blickend"></div>
  <p class="horse-label horse-label-left">SOLVINA</p>
  <p class="horse-label horse-label-right">BELLIS</p>

  <div class="portrait-ring"></div>
  <div class="portrait" role="img" aria-label="Porträt von Veronika"></div>

  <h2 class="memorial-heading">In Memoriam</h2>
  <p class="dates">DATEN :&nbsp; 20.11.1980 - <sup>†</sup>15.05.2024</p>

  <h3 class="section-title section-families">UNSERE FAMILIEN</h3>
  <div class="person family" style="left:205px"><div class="person-photo" role="img" aria-label="Porträt von Gerhard"></div><p class="person-name">GERHARD</p></div>
  <div class="person family" style="left:465px"><div class="person-photo" role="img" aria-label="Porträt von Henrik"></div><p class="person-name">HENRIK</p></div>
  <div class="person family" style="left:725px"><div class="person-photo" role="img" aria-label="Porträt von Frieda"></div><p class="person-name">FRIEDA</p></div>

  <h3 class="section-title section-helpers">UNSERE HELFER</h3>
  <div class="person helper" style="left:143px"><div class="person-photo" role="img" aria-label="Porträt von Dieter"></div><p class="person-name">DIETER</p></div>
  <div class="person helper" style="left:357px"><div class="person-photo" role="img" aria-label="Porträt von Helene"></div><p class="person-name">HELENE</p></div>
  <div class="person helper" style="left:571px"><div class="person-photo" role="img" aria-label="Porträt von Uschi"></div><p class="person-name">USCHI</p></div>
  <div class="person helper" style="left:785px"><div class="person-photo" role="img" aria-label="Porträt von Glenn"></div><p class="person-name">GLENN</p></div>

  <h3 class="thanks-heading">WIR BEDANKEN UNS BEI:</h3>
  <p class="thanks-text">Klaus &amp; Ingrid für die wertvolle Unterstützung, bei Hanni für die Hilfe und Tipps im Umgang mit dem Pferd. Ebenfalls bedanken wir uns bei Familie Weibel, vor allem bei Beni &amp; Sabine und Flori &amp; Greta, dass wir dieses Paradies nach unseren Vorstellungen schaffen durften und für die bauliche Umsetzung. Und natürlich die vielen anderen Helfer und Trostspender.</p>
</main>
</body>
</html>
```